Health software company called BRIGHT MERIDIAN, committed to innovation and technological excellence

The powerpoint presentation template is necessary, very necessary is elegant and modern with innovative images and the color palette attached. The presentation will be used for the business plan and investor presentations that we will use to raise funds. Please, recommend a modern typeface, as well as format to be able to use it and incorporate it as part of the company's brand guidelines. Great diversity of technological solutions
Updates

Very low attendance of designers for a high budget. Very few proposals and no capture my interest

Need extra days to review

Need extra days to review

Need extra days to review

Target Market(s)

managers, managers of public and private health centers, government states, investors

Industry/Entity Type

It Company

Font styles to use
Serif

Requirements
Must have
• The powerpoint presentation template is necessary, very necessary is elegant, minimalist and modern with innovative images and the color palette attached. it must be refined in demarcated style
Nice to have
• very nice, visually harmonic avoid saturation
Should not have
• NO dark colors NO dark colors NO dark colors NO dark colors NO dark colors

```html
<!DOCTYPE html>
<html lang="en">
<head>
<meta charset="utf-8">
<title>Bright Meridian — Presentation Template Overview</title>
<link href="https://fonts.googleapis.com/css2?family=Questrial&display=swap" rel="stylesheet">
<style>
:root{
  --bg:#d9d9d9;
  --white:#ffffff;
  --blue:#1f8fe8;
  --navy:#2c5ea8;
  --mint:#b8f6ef;
  --mint-soft:#dffbf8;
  --aqua:#5fe0d3;
  --ink:#3d4b5c;
  --grey:#8e99a5;
  --line:#cfd8df;
}
*{box-sizing:border-box;margin:0;padding:0}
html,body{width:1200px;height:4000px;overflow:hidden;background:var(--bg)}
body{position:relative;font-family:"Questrial",sans-serif;color:var(--ink)}
.slide{position:absolute;width:384px;height:218px;background:var(--white);overflow:hidden;box-shadow:0 1px 3px rgba(0,0,0,.15)}
.slide::after{content:"";position:absolute;left:0;right:0;bottom:0;height:4px;background:var(--mint)}
.abs{position:absolute}
.photo{position:absolute}
.ph-blue{background:linear-gradient(135deg,#3a7fc4,#9ec9ea)}
.ph-med{background:linear-gradient(135deg,#cfe6f2,#8fb7cf)}
.ph-office{background:linear-gradient(135deg,#dfe4ea,#9aa8b6)}
.ph-city{background:linear-gradient(135deg,#5a9fc6,#c7e3ef)}
.ph-light{background:linear-gradient(135deg,#eef2f5,#c6d2dc)}
.ph-teal{background:linear-gradient(135deg,#9fe9e1,#4fb9c7)}
.ph-tech{background:linear-gradient(135deg,#1d4f6b,#3aa0c0)}
.title{position:absolute;font-size:12px;letter-spacing:.5px;text-transform:uppercase;color:var(--blue)}
.title b{font-weight:400;color:var(--ink)}
.small{font-size:5px;line-height:1.4;color:var(--grey)}
.tiny{font-size:4.5px;line-height:1.35;color:var(--grey)}
.label{font-size:6px;color:var(--blue)}
.box-blue{position:absolute;background:var(--blue);color:#fff}
.section-no{font-size:14px}
.section-name{font-size:20px;line-height:1.05;text-transform:uppercase}
.list{font-size:5.5px;line-height:1.45;list-style:disc;padding-left:8px}
.mint-bg{background:var(--mint)}
.frame{position:absolute;border:2px solid #9fb3c4;border-right:none}
.divider-title{position:absolute;font-size:24px;color:#7f95a8;text-transform:uppercase;line-height:1}
.dot{position:absolute;border-radius:50%}
.bar{position:absolute}
table{border-collapse:collapse}
</style>
</head>
<body>

<!-- Row 1 -->
<section class="slide" style="left:199px;top:26px">
  <div class="photo ph-blue" style="inset:0" role="img" aria-label="Hand touching a glowing digital circuit interface"></div>
  <div class="box-blue" style="left:218px;top:100px;width:150px;height:56px;padding:8px 12px">
    <div style="font-size:11px">Think and Dream</div>
    <div style="font-size:24px;letter-spacing:2px;color:#0d1f3a">DIGITAL</div>
  </div>
</section>

<section class="slide" style="left:605px;top:26px">
  <div class="photo ph-city" style="left:0;top:0;width:384px;height:118px" role="img" aria-label="City skyline at night with light trails"></div>
  <div class="box-blue" style="left:110px;top:58px;width:180px;height:18px;font-size:11px;text-align:center;line-height:18px;letter-spacing:1px">WELCOME MESSAGE</div>
  <p class="small abs" style="left:56px;top:126px;width:280px;font-size:6px">Add your welcome message here. Share your vision, your goals and what this plan means for the people you serve.</p>
  <div class="label abs" style="right:48px;top:178px">General Manager</div>
</section>

<!-- Row 2 -->
<section class="slide" style="left:9px;top:259px">
  <div class="photo ph-light" style="inset:0" role="img" aria-label="White stairs rising to the right"></div>
  <div class="title" style="left:20px;top:26px;font-size:20px;color:#2fd3b9">AGENDA</div>
  <div class="label abs" style="left:206px;top:48px;color:var(--ink)">04. <span style="color:var(--blue)">WAY FORWARD</span></div>
  <div class="label abs" style="left:132px;top:96px;color:var(--ink)">03. <span style="color:var(--blue)">OUR HARDWORK</span></div>
  <div class="label abs" style="left:92px;top:146px;color:var(--ink)">02. <span style="color:var(--blue)">WHY US?</span></div>
  <div class="label abs" style="left:10px;top:196px;color:var(--ink)">01. <span style="color:var(--blue)">ABOUT US</span></div>
</section>

<section class="slide" style="left:405px;top:259px">
  <div class="abs mint-bg" style="left:0;top:0;width:384px;height:210px"></div>
  <div class="photo ph-office" style="left:170px;top:0;width:214px;height:210px" role="img" aria-label="Team of four business people smiling"></div>
  <div class="box-blue" style="left:10px;top:40px;width:150px;height:140px;padding:10px;color:#0d1f3a">
    <div class="section-no">01.</div>
    <div class="section-name" style="margin-top:10px">About us</div>
    <ul class="list" style="margin-top:10px">
      <li>Our Company</li><li>Our History</li><li>Our Vision</li><li>Our Mission</li><li>Our Commitments</li><li>Our Products and Services</li>
    </ul>
  </div>
</section>

<section class="slide" style="left:801px;top:259px">
  <div class="photo ph-city" style="inset:0" role="img" aria-label="Looking up at glass office towers"></div>
  <div class="abs" style="left:16px;top:84px;font-size:14px;line-height:1.1;color:#fff">ABOUT<br><span style="color:var(--blue)">OUR COMPANY</span></div>
  <div class="abs" style="left:166px;top:72px;width:206px;height:64px;background:rgba(255,255,255,.85);padding:6px 8px;font-size:7px;color:var(--ink);line-height:1.3">Add a short description of the company, its purpose and the value it brings to health centers.</div>
</section>

<!-- Row 3 -->
<section class="slide" style="left:9px;top:490px">
  <div class="title" style="left:150px;top:28px"><b>OUR </b>HISTORY</div>
  <div class="abs" style="left:188px;top:50px;width:1px;height:150px;background:var(--line)"></div>
  <div class="dot" style="left:178px;top:82px;width:20px;height:20px;border:3px solid var(--aqua);background:var(--blue)"></div>
  <div class="dot" style="left:178px;top:142px;width:20px;height:20px;border:3px solid var(--aqua);background:var(--blue)"></div>
  <div class="label abs" style="left:100px;top:80px">Creative Brief</div>
  <p class="tiny abs" style="left:40px;top:89px;width:120px;text-align:right">Add a short note about this milestone and what it meant.</p>
  <div class="label abs" style="left:222px;top:128px">Creative Brief</div>
  <p class="tiny abs" style="left:222px;top:137px;width:120px">Add a short note about this milestone and what it meant.</p>
  <div class="photo ph-office" style="left:250px;top:50px;width:90px;height:58px" role="img" aria-label="Desk with laptop and papers"></div>
  <div class="photo ph-med" style="left:40px;top:140px;width:90px;height:58px" role="img" aria-label="Medical equipment close-up"></div>
</section>

<section class="slide" style="left:405px;top:490px">
  <div class="abs" style="left:192px;top:20px;width:1px;height:180px;background:var(--line)"></div>
  <div class="dot" style="left:182px;top:36px;width:20px;height:20px;border:3px solid var(--aqua);background:var(--blue)"></div>
  <div class="dot" style="left:182px;top:92px;width:20px;height:20px;border:3px solid var(--aqua);background:var(--blue)"></div>
  <div class="dot" style="left:182px;top:148px;width:20px;height:20px;border:3px solid var(--aqua);background:var(--blue)"></div>
  <div class="label abs" style="left:100px;top:18px">Creative Brief</div>
  <p class="tiny abs" style="left:60px;top:27px;width:110px;text-align:right">Add a short note about this step.</p>
  <div class="label abs" style="left:226px;top:76px">Creative Brief</div>
  <p class="tiny abs" style="left:226px;top:85px;width:110px">Add a short note about this step.</p>
  <div class="label abs" style="left:100px;top:132px">Creative Brief</div>
  <p class="tiny abs" style="left:60px;top:141px;width:110px;text-align:right">Add a short note about this step.</p>
  <div class="photo ph-office" style="left:80px;top:76px;width:90px;height:50px" role="img" aria-label="Laptop on a desk"></div>
  <div class="photo ph-office" style="left:226px;top:128px;width:100px;height:60px" role="img" aria-label="Team stacking hands together"></div>
  <div class="box-blue" style="left:174px;top:196px;width:36px;height:8px;font-size:5px;text-align:center;line-height:8px">FUTURE</div>
</section>

<section class="slide" style="left:801px;top:490px">
  <div class="photo ph-med" style="inset:0" role="img" aria-label="Doctor touching a hexagon medical interface"></div>
  <div class="abs" style="left:236px;top:64px;font-size:17px;color:var(--ink)">OUR <span style="color:var(--blue)">VISION</span></div>
  <p class="abs" style="left:236px;top:88px;width:130px;font-size:6px;color:var(--ink);line-height:1.35">Add your vision statement here in one or two lines.</p>
</section>

<!-- Row 4 -->
<section class="slide" style="left:9px;top:719px">
  <div class="photo ph-med" style="inset:0" role="img" aria-label="Doctor holding a tablet with medical icons"></div>
  <div class="abs" style="left:14px;top:80px;font-size:17px;color:var(--ink)">OUR <span style="color:var(--blue)">MISSION</span></div>
  <p class="abs" style="left:14px;top:104px;width:150px;font-size:5.5px;color:var(--ink);line-height:1.35">Add your mission statement here, focused on care, access and trusted technology for health.</p>
</section>

<section class="slide" style="left:405px;top:719px">
  <div class="abs" style="left:-50px;top:96px;transform:rotate(-90deg);font-size:12px;letter-spacing:1px;color:var(--ink);width:150px;text-align:center">OUR <span style="color:var(--blue)">COMMITMENTS</span></div>
  <svg class="abs" style="left:30px;top:20px" width="340" height="180" viewBox="0 0 340 180">
    <g fill="#2ab5c8">
      <rect x="4" y="8" width="18" height="18" rx="3"/><rect x="4" y="34" width="18" height="18" rx="3" fill="#3aa0d8"/>
      <rect x="4" y="60" width="18" height="18" rx="3" fill="#2f86d6"/><rect x="4" y="86" width="18" height="18" rx="3" fill="#2f6fc8"/>
      <rect x="4" y="112" width="18" height="18" rx="3" fill="#3b5fb8"/><rect x="4" y="138" width="18" height="18" rx="3" fill="#4a56a8"/>
    </g>
    <g fill="none" stroke="#2f86d6" stroke-width="3">
      <path d="M30 88 H320"/>
      <path d="M90 88 C90 40 100 40 100 22"/><path d="M150 88 C150 40 160 40 160 22"/><path d="M220 88 C220 60 230 60 240 50"/>
      <path d="M90 88 C90 130 100 130 100 150" stroke="#3b5fb8"/><path d="M150 88 C150 130 160 130 160 150" stroke="#3b5fb8"/>
    </g>
    <g fill="#fff" stroke="#2ab5c8" stroke-width="2">
      <circle cx="100" cy="22" r="6"/><circle cx="160" cy="22" r="6"/><circle cx="240" cy="50" r="6"/>
      <circle cx="100" cy="150" r="6"/><circle cx="160" cy="150" r="6"/><circle cx="320" cy="88" r="6"/>
    </g>
  </svg>
  <div class="label abs" style="left:105px;top:24px">INSERT TITLE</div>
  <div class="label abs" style="left:165px;top:24px">INSERT TITLE</div>
  <div class="label abs" style="left:250px;top:56px">INSERT TITLE</div>
  <div class="label abs" style="left:105px;top:152px">INSERT TITLE</div>
  <div class="label abs" style="left:165px;top:152px">INSERT TITLE</div>
</section>

<section class="slide" style="left:801px;top:719px">
  <div class="title" style="left:130px;top:16px;font-size:15px"><b>OUR </b>SERVICES</div>
  <div class="abs" style="left:112px;top:56px;width:46px;height:46px;background:#1f8fe8;color:#fff;font-size:9px;display:flex;align-items:center;justify-content:center">TITLE</div>
  <div class="abs" style="left:164px;top:66px;width:40px;height:40px;background:#5fe0d3;color:#fff;font-size:9px;display:flex;align-items:center;justify-content:center">TITLE</div>
  <div class="abs" style="left:210px;top:54px;width:44px;height:44px;background:#2ab5c8;color:#fff;font-size:9px;display:flex;align-items:center;justify-content:center">TITLE</div>
  <div class="abs" style="left:146px;top:110px;width:44px;height:44px;background:#f6c94a;color:#fff;font-size:9px;display:flex;align-items:center;justify-content:center">TITLE</div>
  <div class="abs" style="left:100px;top:130px;width:40px;height:40px;background:#7ad27a;color:#fff;font-size:9px;display:flex;align-items:center;justify-content:center">TITLE</div>
  <div class="abs" style="left:126px;top:158px;width:44px;height:40px;background:#2f6fc8;color:#fff;font-size:9px;display:flex;align-items:center;justify-content:center">TITLE</div>
  <div class="abs" style="left:196px;top:124px;width:44px;height:44px;background:#f6d36a;color:#fff;font-size:9px;display:flex;align-items:center;justify-content:center">TITLE</div>
  <div class="abs" style="left:52px;top:100px;width:22px;height:22px;background:#f28b5b"></div>
  <div class="abs" style="left:60px;top:150px;width:18px;height:18px;background:#4fb9c7"></div>
</section>

<!-- Row 5 -->
<section class="slide" style="left:9px;top:950px">
  <div class="abs mint-bg" style="left:0;top:0;width:384px;height:210px"></div>
  <div class="photo ph-office" style="left:130px;top:22px;width:254px;height:166px" role="img" aria-label="Hand pointing at charts on a tablet"></div>
  <div class="abs" style="left:16px;top:50px;color:#0d1f3a">
    <div class="section-no">02.</div>
    <div class="section-name" style="margin-top:4px">Why us?</div>
    <ul class="list" style="margin-top:6px">
      <li>Our Differences</li><li>Our Works</li><li>Our Smartphone Mockup</li><li>Our Laptop Mockup</li><li>Our Incredible Team</li>
    </ul>
  </div>
</section>

<section class="slide" style="left:405px;top:950px">
  <div class="title" style="left:14px;top:14px"><b>OUR </b>DIFFERENCES</div>
  <div class="abs" style="left:40px;top:46px;width:50px;height:40px;background:#5fe0d3;color:#fff;font-size:16px;text-align:center;line-height:40px;border-radius:6px">1</div>
  <div class="abs" style="left:118px;top:46px;width:50px;height:40px;background:#2ab5c8;color:#fff;font-size:16px;text-align:center;line-height:40px;border-radius:6px">2</div>
  <div class="abs" style="left:196px;top:46px;width:50px;height:40px;background:#1f8fe8;color:#fff;font-size:16px;text-align:center;line-height:40px;border-radius:6px">3</div>
  <div class="abs" style="left:274px;top:46px;width:50px;height:40px;background:#2c5ea8;color:#fff;font-size:16px;text-align:center;line-height:40px;border-radius:6px">4</div>
  <div class="tiny abs" style="left:36px;top:96px;width:60px;text-align:center">Insert title here</div>
  <div class="tiny abs" style="left:114px;top:96px;width:60px;text-align:center">Insert title here</div>
  <div class="tiny abs" style="left:192px;top:96px;width:60px;text-align:center">Insert title here</div>
  <div class="tiny abs" style="left:270px;top:96px;width:60px;text-align:center">Insert title here</div>
  <div class="photo ph-light" style="left:110px;top:128px;width:120px;height:72px" role="img" aria-label="Stack of puzzle pieces with one blue piece"></div>
</section>

<section class="slide" style="left:801px;top:950px">
  <div class="title" style="left:14px;top:10px"><b>OUR </b>ACHIEVEMENTS</div>
  <p class="tiny abs" style="left:14px;top:26px;width:356px;font-size:5.5px">Add a short summary of your key achievements and results for the year here.</p>
  <div class="bar" style="left:108px;top:66px;width:150px;height:17px;background:#4fd3c8"></div>
  <div class="bar" style="left:108px;top:86px;width:170px;height:17px;background:#2ab5c8"></div>
  <div class="bar" style="left:108px;top:106px;width:190px;height:17px;background:#1f8fe8"></div>
  <div class="bar" style="left:108px;top:126px;width:210px;height:17px;background:#2f6fc8"></div>
  <div class="bar" style="left:108px;top:146px;width:230px;height:17px;background:#3b5fb8"></div>
  <div class="bar" style="left:108px;top:166px;width:250px;height:17px;background:#5a56b0"></div>
  <svg class="abs" style="left:300px;top:40px" width="60" height="40"><path d="M4 36 L40 10 L36 4 L56 4 L52 22 L46 16 L12 36Z" fill="#2ab5c8"/></svg>
  <div class="abs" style="left:76px;top:70px;width:10px;height:110px;display:flex;flex-direction:column;gap:10px">
    <span style="width:9px;height:9px;border-radius:50%;background:var(--ink)"></span><span style="width:9px;height:9px;background:var(--ink)"></span><span style="width:9px;height:9px;border-radius:50%;background:var(--ink)"></span><span style="width:9px;height:9px;background:var(--ink)"></span><span style="width:9px;height:9px;border-radius:50%;background:var(--ink)"></span><span style="width:9px;height:9px;background:var(--ink)"></span>
  </div>
</section>

<!-- Row 6 -->
<section class="slide" style="left:9px;top:1184px">
  <div class="title" style="left:148px;top:28px"><b>OUR </b>WORKS</div>
  <div class="photo ph-tech" style="left:24px;top:62px;width:100px;height:56px" role="img" aria-label="Close-up of a circuit board"></div>
  <div class="photo ph-office" style="left:142px;top:62px;width:100px;height:56px" role="img" aria-label="Person working at a desk with papers"></div>
  <div class="photo ph-office" style="left:260px;top:62px;width:100px;height:56px" role="img" aria-label="Team meeting around a table"></div>
  <div class="label abs" style="left:50px;top:134px">BIG DATA</div><div class="abs" style="left:108px;top:126px;font-size:22px;color:#b9ecef">01</div>
  <div class="label abs" style="left:132px;top:134px">PROFESSIONAL CONSULTING</div><div class="abs" style="left:222px;top:126px;font-size:22px;color:#b9ecef">02</div>
  <div class="label abs" style="left:260px;top:134px">APPS DEVELOPMENT</div><div class="abs" style="left:338px;top:126px;font-size:22px;color:#b9ecef">03</div>
  <p class="tiny abs" style="left:30px;top:144px;width:80px">Add a short note here.</p>
  <p class="tiny abs" style="left:140px;top:144px;width:80px">Add a short note here.</p>
  <p class="tiny abs" style="left:260px;top:144px;width:80px">Add a short note here.</p>
</section>

<section class="slide" style="left:405px;top:1184px">
  <div class="title" style="left:148px;top:28px"><b>OUR </b>WORKS</div>
  <div class="photo ph-tech" style="left:24px;top:62px;width:100px;height:56px" role="img" aria-label="Close-up of a circuit board"></div>
  <div class="photo ph-office" style="left:142px;top:62px;width:100px;height:56px" role="img" aria-label="Person working at a desk with papers"></div>
  <div class="photo ph-office" style="left:260px;top:62px;width:100px;height:56px" role="img" aria-label="Team meeting around a table"></div>
  <div class="label abs" style="left:50px;top:134px">BIG DATA</div><div class="abs" style="left:108px;top:126px;font-size:22px;color:#b9ecef">04</div>
  <div class="label abs" style="left:132px;top:134px">PROFESSIONAL CONSULTING</div><div class="abs" style="left:222px;top:126px;font-size:22px;color:#b9ecef">05</div>
  <div class="label abs" style="left:260px;top:134px">APPS DEVELOPMENT</div><div class="abs" style="left:338px;top:126px;font-size:22px;color:#b9ecef">06</div>
  <p class="tiny abs" style="left:30px;top:144px;width:80px">Add a short note here.</p>
  <p class="tiny abs" style="left:140px;top:144px;width:80px">Add a short note here.</p>
  <p class="tiny abs" style="left:260px;top:144px;width:80px">Add a short note here.</p>
</section>

<section class="slide" style="left:801px;top:1184px">
  <div class="abs mint-bg" style="left:0;top:70px;width:384px;height:46px"></div>
  <div class="photo ph-light" style="left:36px;top:20px;width:66px;height:176px;border-radius:10px" role="img" aria-label="Smartphone showing an app screen"></div>
  <div class="dot" style="left:110px;top:90px;width:50px;height:50px;background:var(--blue);color:#fff;font-size:12px;text-align:center;line-height:50px">97%</div>
  <div class="abs" style="left:170px;top:34px;font-size:15px;line-height:1.05;color:#7f95a8">MOBILE<br><span style="color:var(--blue)">MOCKUP</span></div>
  <p class="tiny abs" style="left:170px;top:72px;width:190px;font-size:5.5px;color:var(--ink)">Show your app on a phone screen and describe the key features here.</p>
  <div class="dot" style="left:176px;top:120px;width:28px;height:28px;border:2px solid var(--ink)"></div>
  <div class="dot" style="left:176px;top:160px;width:28px;height:28px;border:2px solid var(--ink)"></div>
  <div class="label abs" style="left:212px;top:124px;color:var(--ink)">Insert title here</div>
  <div class="label abs" style="left:212px;top:164px;color:var(--ink)">Insert title here</div>
</section>

<!-- Row 7 -->
<section class="slide" style="left:9px;top:1422px">
  <div class="abs mint-bg" style="inset:0"></div>
  <div class="abs" style="left:200px;top:0;width:184px;height:218px;background:#c8f8f2"></div>
  <div class="abs" style="left:28px;top:26px;font-size:14px;color:#7f95a8">LAPTOP <span style="color:var(--blue)">MOCKUP</span></div>
  <div class="abs" style="left:36px;top:58px;width:110px">
    <div class="label" style="color:var(--ink)">Insert title here</div><p class="tiny" style="margin-bottom:12px">Add a short note here.</p>
    <div class="label" style="color:var(--ink)">Insert title here</div><p class="tiny" style="margin-bottom:12px">Add a short note here.</p>
    <div class="label" style="color:var(--ink)">Insert title here</div><p class="tiny" style="margin-bottom:12px">Add a short note here.</p>
    <div class="label" style="color:var(--ink)">Insert title here</div><p class="tiny">Add a short note here.</p>
  </div>
  <div class="abs" style="left:130px;top:70px;font-size:18px;color:#9bb0c0;line-height:34px">1<br>2<br>3<br>4</div>
  <div class="photo ph-light" style="left:216px;top:56px;width:140px;height:110px" role="img" aria-label="Desktop monitor with keyboard and mouse"></div>
</section>

<section class="slide" style="left:405px;top:1422px">
  <div class="abs" style="left:130px;top:0;width:254px;height:218px;background:var(--mint-soft)"></div>
  <div class="title" style="left:16px;top:10px"><b>THE </b>TEAM</div>
  <div class="dot photo ph-office" style="left:20px;top:56px;width:90px;height:90px" role="img" aria-label="Portrait of a team member"></div>
  <div class="label abs" style="left:44px;top:156px;color:var(--ink)">Noel Vance</div>
  <div class="dot photo ph-office" style="left:150px;top:28px;width:56px;height:56px" role="img" aria-label="Portrait of a team member"></div>
  <div class="label abs" style="left:156px;top:88px;color:var(--ink)">Leo Marsh</div>
  <div class="dot photo ph-office" style="left:264px;top:28px;width:56px;height:56px" role="img" aria-label="Portrait of a team member"></div>
  <div class="label abs" style="left:274px;top:88px;color:var(--ink)">Ian Pell</div>
  <div class="dot photo ph-office" style="left:150px;top:118px;width:56px;height:56px" role="img" aria-label="Portrait of a team member"></div>
  <div class="label abs" style="left:156px;top:178px;color:var(--ink)">Ada Reyes</div>
  <div class="dot photo ph-office" style="left:264px;top:118px;width:56px;height:56px" role="img" aria-label="Portrait of a team member"></div>
  <div class="label abs" style="left:272px;top:178px;color:var(--ink)">Tess Lowe</div>
</section>

<section class="slide" style="left:801px;top:1422px">
  <div class="abs mint-bg" style="inset:0"></div>
  <div class="title" style="left:16px;top:10px;color:#fff">MEET THE TEAM</div>
  <div class="abs" style="left:14px;top:40px;width:110px;height:160px;background:#e4fcf9"></div>
  <div class="abs" style="left:137px;top:40px;width:110px;height:160px;background:#e4fcf9"></div>
  <div class="abs" style="left:260px;top:40px;width:110px;height:160px;background:#e4fcf9"></div>
  <div class="dot photo ph-office" style="left:40px;top:40px;width:48px;height:48px" role="img" aria-label="Portrait of a team member"></div>
  <div class="dot photo ph-office" style="left:162px;top:40px;width:48px;height:48px" role="img" aria-label="Portrait of a team member"></div>
  <div class="dot photo ph-office" style="left:286px;top:40px;width:48px;height:48px" role="img" aria-label="Portrait of a team member"></div>
  <div class="label abs" style="left:30px;top:96px;color:var(--ink)">Owen Hale</div>
  <div class="label abs" style="left:162px;top:96px;color:var(--ink)">Ravi Lund</div>
  <div class="label abs" style="left:280px;top:96px;color:var(--ink)">Paul Greer</div>
  <div class="bar" style="left:22px;top:130px;width:90px;height:4px;background:var(--blue)"></div>
  <div class="bar" style="left:22px;top:150px;width:70px;height:4px;background:var(--blue)"></div>
  <div class="bar" style="left:145px;top:130px;width:80px;height:4px;background:var(--blue)"></div>
  <div class="bar" style="left:145px;top:150px;width:95px;height:4px;background:var(--blue)"></div>
  <div class="bar" style="left:268px;top:130px;width:92px;height:4px;background:var(--blue)"></div>
  <div class="bar" style="left:268px;top:150px;width:74px;height:4px;background:var(--blue)"></div>
</section>

<!-- Row 8 -->
<section class="slide" style="left:9px;top:1661px">
  <div class="photo ph-med" style="left:0;top:0;width:240px;height:210px" role="img" aria-label="Doctor with stethoscope in a hospital"></div>
  <div class="box-blue" style="left:228px;top:50px;width:146px;height:140px;padding:10px;background:var(--navy)">
    <div class="section-no">03.</div>
    <div class="section-name" style="margin-top:6px">Our<br>Hardwork</div>
    <ul class="list" style="margin-top:6px"><li>Our Awesome Partners</li><li>Our Awesome Clients</li><li>Our Customers Say</li><li>Our Sales</li><li>Our Profits</li></ul>
  </div>
</section>

<section class="slide" style="left:405px;top:1661px">
  <div class="photo ph-med" style="inset:0" role="img" aria-label="Surgeons in masks in an operating room"></div>
  <div class="abs" style="left:0;top:0;width:180px;height:110px;background:linear-gradient(135deg,rgba(255,255,255,.9),rgba(255,255,255,.3))"></div>
  <div class="abs" style="left:20px;top:22px;font-size:13px;color:var(--ink);line-height:1.1">OUR AWESOME<br><span style="color:var(--blue)">PARTNER</span></div>
</section>

<section class="slide" style="left:801px;top:1661px">
  <div class="photo ph-blue" style="left:0;top:0;width:240px;height:218px" role="img" aria-label="Finger touching a network of connected people icons"></div>
  <div class="abs" style="left:240px;top:0;width:144px;height:218px;background:#2f7fb4"></div>
  <div class="abs" style="left:250px;top:14px;font-size:13px;color:#fff;line-height:1.1;text-align:right;width:126px">OUR AWESOME<br><span style="color:var(--mint)">CLIENTS</span></div>
  <div class="abs" style="left:260px;top:60px;font-size:5.5px;color:#fff;width:110px;text-align:right">CLIENTS LOGO LIST</div>
</section>

<!-- Row 9 -->
<section class="slide" style="left:9px;top:1906px">
  <div class="title" style="left:16px;top:14px"><b>CLIENT </b>DATA &amp; PROFITS</div>
  <svg class="abs" style="left:20px;top:44px" width="350" height="80" viewBox="0 0 350 80">
    <g fill="none" stroke-width="6">
      <circle cx="40" cy="40" r="30" stroke="#dfeff4"/><circle cx="40" cy="40" r="30" stroke="#5fe0d3" stroke-dasharray="134 188" transform="rotate(-90 40 40)"/>
      <circle cx="130" cy="40" r="30" stroke="#dfeff4"/><circle cx="130" cy="40" r="30" stroke="#5fe0d3" stroke-dasharray="88 188" transform="rotate(-90 130 40)"/>
      <circle cx="220" cy="40" r="30" stroke="#dfeff4"/><circle cx="220" cy="40" r="30" stroke="#5fe0d3" stroke-dasharray="151 188" transform="rotate(-90 220 40)"/>
      <circle cx="310" cy="40" r="30" stroke="#dfeff4"/><circle cx="310" cy="40" r="30" stroke="#5fe0d3" stroke-dasharray="53 188" transform="rotate(-90 310 40)"/>
    </g>
    <g font-family="Questrial,sans-serif" font-size="12" fill="#3d4b5c" text-anchor="middle">
      <text x="40" y="44">71%</text><text x="130" y="44">47%</text><text x="220" y="44">80%</text><text x="310" y="44">28%</text>
    </g>
  </svg>
  <div class="tiny abs" style="left:36px;top:134px;width:56px;text-align:center;color:var(--ink)">Add title here</div>
  <div class="tiny abs" style="left:126px;top:134px;width:56px;text-align:center;color:var(--ink)">Add title here</div>
  <div class="tiny abs" style="left:216px;top:134px;width:56px;text-align:center;color:var(--ink)">Add title here</div>
  <div class="tiny abs" style="left:306px;top:134px;width:56px;text-align:center;color:var(--ink)">Add title here</div>
  <p class="tiny abs" style="left:24px;top:176px;width:336px;text-align:center;font-size:5.5px">Add a short summary of client growth and profit for the period here.</p>
</section>

<section class="slide" style="left:405px;top:1906px">
  <div class="photo ph-light" style="inset:0" role="img" aria-label="Doctor smiling in a bright clinic"></div>
  <div class="abs" style="left:20px;top:60px;font-size:10px;color:var(--ink)">OUR <span style="color:var(--blue)">CUSTOMER SAYS</span></div>
  <p class="abs" style="left:20px;top:124px;width:170px;font-size:6px;color:var(--ink);line-height:1.35">Add a short customer quote about working with the team here.</p>
  <div class="photo ph-med" style="left:212px;top:100px;width:130px;height:74px" role="img" aria-label="Nurse talking with an older patient"></div>
</section>

<section class="slide" style="left:801px;top:1906px">
  <div class="abs mint-bg" style="inset:0"></div>
  <div class="frame" style="left:80px;top:60px;width:100px;height:90px"></div>
  <div class="divider-title" style="left:120px;top:70px">OUR<br>DATA <span style="font-size:14px;color:var(--blue)">&#9650;</span></div>
</section>

<!-- Row 10 -->
<section class="slide" style="left:9px;top:2157px">
  <div class="dot" style="left:148px;top:72px;width:74px;height:74px;border:4px solid #cfe8f7;background:#fff;text-align:center;line-height:66px;font-size:11px;color:var(--blue)"><b style="font-weight:400;color:var(--ink)">OUR </b>SALES</div>
  <div class="label abs" style="left:166px;top:40px;color:var(--ink)">PRODUCT 1</div>
  <div class="label abs" style="left:236px;top:56px;color:var(--ink)">PRODUCT 2</div>
  <div class="label abs" style="left:238px;top:96px;color:var(--ink)">PRODUCT 3</div>
  <div class="label abs" style="left:236px;top:136px;color:var(--ink)">PRODUCT 4</div>
  <div class="label abs" style="left:176px;top:178px;color:var(--ink)">PRODUCT 5</div>
  <div class="label abs" style="left:102px;top:150px;color:var(--ink)">PRODUCT 6</div>
  <div class="label abs" style="left:86px;top:110px;color:var(--ink)">PRODUCT 7</div>
  <div class="label abs" style="left:90px;top:60px;color:var(--ink)">PRODUCT 8</div>
  <svg class="abs" style="left:20px;top:100px" width="60" height="36"><g fill="#2f86d6"><rect x="2" y="16" width="4" height="20"/><rect x="10" y="8" width="4" height="28" fill="#5fe0d3"/><rect x="18" y="20" width="4" height="16"/><rect x="26" y="4" width="4" height="32" fill="#5fe0d3"/><rect x="34" y="12" width="4" height="24"/><rect x="42" y="18" width="4" height="18"/></g></svg>
  <svg class="abs" style="left:320px;top:100px" width="44" height="44"><circle cx="22" cy="22" r="18" fill="#2f86d6"/><path d="M22 22 L22 4 A18 18 0 0 1 40 22Z" fill="#f6a24a"/><path d="M22 22 L40 22 A18 18 0 0 1 30 38Z" fill="#5fe0d3"/></svg>
</section>

<section class="slide" style="left:405px;top:2157px">
  <div class="title" style="left:14px;top:10px"><b>OUR </b>PROFIT</div>
  <svg class="abs" style="left:30px;top:30px" width="330" height="130" viewBox="0 0 330 130">
    <g stroke="#eef2f5"><path d="M20 20H320M20 44H320M20 68H320M20 92H320M20 116H320"/></g>
    <g fill="#5fe0d3">
      <rect x="30" y="110" width="6" height="6"/><rect x="54" y="106" width="6" height="10"/><rect x="78" y="108" width="6" height="8"/><rect x="102" y="100" width="6" height="16"/>
      <rect x="126" y="104" width="6" height="12"/><rect x="150" y="96" width="6" height="20"/><rect x="174" y="100" width="6" height="16"/><rect x="198" y="94" width="6" height="22"/>
      <rect x="222" y="98" width="6" height="18"/><rect x="246" y="90" width="6" height="26"/><rect x="270" y="96" width="6" height="20"/><rect x="294" y="92" width="6" height="24"/>
    </g>
    <g fill="#1f8fe8">
      <rect x="38" y="104" width="6" height="12"/><rect x="62" y="96" width="6" height="20"/><rect x="86" y="100" width="6" height="16"/><rect x="110" y="84" width="6" height="32"/>
      <rect x="134" y="90" width="6" height="26"/><rect x="158" y="76" width="6" height="40"/><rect x="182" y="82" width="6" height="34"/><rect x="206" y="66" width="6" height="50"/>
      <rect x="230" y="74" width="6" height="42"/><rect x="254" y="50" width="6" height="66"/><rect x="278" y="60" width="6" height="56"/><rect x="302" y="26" width="6" height="90"/>
    </g>
  </svg>
  <p class="tiny abs" style="left:24px;top:170px;width:336px;text-align:center;font-size:5.5px">Add a short note on profit growth across the year here.</p>
</section>

<section class="slide" style="left:801px;top:2157px">
  <div class="abs mint-bg" style="inset:0"></div>
  <div class="frame" style="left:80px;top:60px;width:100px;height:90px"></div>
  <div class="divider-title" style="left:120px;top:72px">PROJECT<br>MANAGEMENT <span style="font-size:14px;color:var(--blue)">&#9776;</span></div>
</section>

<!-- Row 11 -->
<section class="slide" style="left:9px;top:2395px">
  <div class="title" style="left:14px;top:14px"><b>PROJECT </b>OVERVIEW</div>
  <p class="tiny abs" style="left:36px;top:34px;width:312px;text-align:center;font-size:5.5px">Add a short overview of the project, its scope and main goals here.</p>
  <svg class="abs" style="left:40px;top:70px" width="310" height="40">
    <g fill="#fff" stroke="#5fe0d3" stroke-width="2"><circle cx="16" cy="20" r="14"/><circle cx="96" cy="20" r="14"/><circle cx="176" cy="20" r="14"/><circle cx="256" cy="20" r="14"/></g>
    <g fill="#1f8fe8"><path d="M48 16h10v-4l8 8-8 8v-4H48z"/><path d="M128 16h10v-4l8 8-8 8v-4h-10z"/><path d="M208 16h10v-4l8 8-8 8v-4h-10z"/><path d="M280 16h10v-4l8 8-8 8v-4h-10z"/></g>
  </svg>
  <div class="label abs" style="left:36px;top:118px">The subtitle</div>
  <div class="label abs" style="left:116px;top:118px">The subtitle</div>
  <div class="label abs" style="left:196px;top:118px">The subtitle</div>
  <div class="label abs" style="left:276px;top:118px">The subtitle</div>
  <div class="abs" style="left:108px;top:130px;width:1px;height:60px;background:var(--line)"></div>
  <div class="abs" style="left:188px;top:130px;width:1px;height:60px;background:var(--line)"></div>
  <div class="abs" style="left:268px;top:130px;width:1px;height:60px;background:var(--line)"></div>
  <p class="tiny abs" style="left:36px;top:134px;width:64px">Add a short point.</p>
  <p class="tiny abs" style="left:116px;top:134px;width:64px">Add a short point.</p>
  <p class="tiny abs" style="left:196px;top:134px;width:64px">Add a short point.</p>
  <p class="tiny abs" style="left:276px;top:134px;width:64px">Add a short point.</p>
</section>

<section class="slide" style="left:405px;top:2395px">
  <div class="title" style="left:14px;top:12px"><b>PROJECT </b>PHASE</div>
  <p class="tiny abs" style="left:14px;top:26px;width:350px;font-size:5.5px">Add a short description of each phase of the project here.</p>
  <div class="abs" style="left:24px;top:100px;width:336px;height:10px;display:flex;font-size:5px;color:#fff;text-align:center;line-height:10px">
    <span style="flex:1;background:#d7f6f3;color:var(--ink)">PHASE 1</span><span style="flex:1;background:#b8f0ea;color:var(--ink)">PHASE 2</span><span style="flex:1;background:#5fe0d3">PHASE 3</span><span style="flex:1;background:#2ab5c8">PHASE 4</span><span style="flex:1;background:#1f8fe8">PHASE 5</span><span style="flex:1;background:#2c5ea8">PHASE 6</span>
  </div>
  <div class="abs" style="left:24px;top:60px;width:50px;height:24px;border:1px solid #b8e6f3;font-size:5px;color:var(--blue);text-align:center;padding-top:3px">The subtitle</div>
  <div class="abs" style="left:138px;top:60px;width:50px;height:24px;border:1px solid #b8e6f3;font-size:5px;color:var(--blue);text-align:center;padding-top:3px">The subtitle</div>
  <div class="abs" style="left:250px;top:60px;width:50px;height:24px;border:1px solid #b8e6f3;font-size:5px;color:var(--blue);text-align:center;padding-top:3px">The subtitle</div>
  <div class="abs" style="left:80px;top:126px;width:50px;height:24px;border:1px solid #b8e6f3;font-size:5px;color:var(--blue);text-align:center;padding-top:3px">The subtitle</div>
  <div class="abs" style="left:194px;top:126px;width:50px;height:24px;border:1px solid #b8e6f3;font-size:5px;color:var(--blue);text-align:center;padding-top:3px">The subtitle</div>
  <div class="abs" style="left:306px;top:126px;width:50px;height:24px;border:1px solid #b8e6f3;font-size:5px;color:var(--blue);text-align:center;padding-top:3px">The subtitle</div>
  <div class="dot" style="left:43px;top:86px;width:12px;height:12px;border:1px solid var(--ink)"></div>
  <div class="dot" style="left:157px;top:86px;width:12px;height:12px;border:1px solid var(--ink)"></div>
  <div class="dot" style="left:269px;top:86px;width:12px;height:12px;border:1px solid var(--ink)"></div>
  <div class="dot" style="left:99px;top:154px;width:12px;height:12px;border:1px solid var(--ink)"></div>
  <div class="dot" style="left:213px;top:154px;width:12px;height:12px;border:1px solid var(--ink)"></div>
  <div class="dot" style="left:325px;top:154px;width:12px;height:12px;border:1px solid var(--ink)"></div>
</section>

<section class="slide" style="left:801px;top:2395px">
  <div class="title" style="left:14px;top:12px"><b>PROJECT </b>MONTHLY TIMELINE</div>
  <p class="tiny abs" style="left:14px;top:26px;width:350px;font-size:5.5px">Add a short note about the monthly plan for the project here.</p>
  <div class="abs" style="left:24px;top:104px;width:340px;height:10px;display:flex;font-size:5px;color:var(--ink);text-align:center;line-height:10px">
    <span style="flex:1;background:#e9fbf9">Jan – Feb</span><span style="flex:1;background:#d7f6f3">Mar – Apr</span><span style="flex:1;background:#b8f0ea">May – June</span><span style="flex:1;background:#8ee8df">July – Aug</span><span style="flex:1;background:#5fe0d3;color:#fff">Sept – Oct</span><span style="flex:1;background:#2ab5c8;color:#fff">Nov – Dec</span>
  </div>
  <div class="dot" style="left:40px;top:70px;width:26px;height:26px;border:1px solid #9fe9e1"></div>
  <div class="dot" style="left:152px;top:70px;width:26px;height:26px;border:1px solid #9fe9e1"></div>
  <div class="dot" style="left:264px;top:70px;width:26px;height:26px;border:1px solid #9fe9e1"></div>
  <div class="dot" style="left:96px;top:124px;width:26px;height:26px;border:1px solid #9fe9e1"></div>
  <div class="dot" style="left:208px;top:124px;width:26px;height:26px;border:1px solid #9fe9e1"></div>
  <div class="dot" style="left:320px;top:124px;width:26px;height:26px;border:1px solid #9fe9e1"></div>
</section>

<!-- Row 12 -->
<section class="slide" style="left:9px;top:2643px">
  <div class="title" style="left:14px;top:12px"><b>PROJECT </b>WEEKLY TIMELINE</div>
  <p class="tiny abs" style="left:14px;top:26px;width:350px;font-size:5.5px">Add a short note about the weekly plan here.</p>
  <div class="abs" style="left:24px;top:46px;width:340px;height:8px;background:#e4f2fb"></div>
  <div class="tiny abs" style="left:30px;top:47px;color:var(--ink)">Task Name</div>
  <div class="abs" style="left:136px;top:46px;width:1px;height:140px;background:var(--line)"></div>
  <div class="tiny abs" style="left:28px;top:60px;width:100px;line-height:2.4">First task here<br>Second task here<br>Third task here<br>Fourth task here<br>Fifth task here<br>Sixth task here</div>
  <div class="bar" style="left:150px;top:62px;width:40px;height:5px;background:#5fe0d3"></div>
  <div class="bar" style="left:180px;top:72px;width:60px;height:5px;background:#1f8fe8"></div>
  <div class="bar" style="left:170px;top:84px;width:30px;height:5px;background:#2c5ea8"></div>
  <div class="bar" style="left:220px;top:96px;width:70px;height:5px;background:#5fe0d3"></div>
  <div class="bar" style="left:250px;top:108px;width:50px;height:5px;background:#1f8fe8"></div>
  <div class="bar" style="left:290px;top:120px;width:60px;height:5px;background:#2c5ea8"></div>
  <div class="bar" style="left:200px;top:132px;width:80px;height:5px;background:#5fe0d3"></div>
  <div class="bar" style="left:310px;top:150px;width:40px;height:5px;background:#1f8fe8"></div>
</section>

<section class="slide" style="left:405px;top:2643px">
  <div class="title" style="left:14px;top:12px"><b>PROJECT </b>RECOMMENDATIONS</div>
  <p class="tiny abs" style="left:14px;top:26px;width:350px;font-size:5.5px">Add a short note about each recommendation here.</p>
  <div class="abs" style="left:44px;top:56px;width:86px;height:134px;border:1px solid #b8e6f3"><div style="background:#d7f6f3;font-size:5px;text-align:center;padding:4px;color:var(--ink)">RECOMMENDATION<br>A</div></div>
  <div class="abs" style="left:148px;top:48px;width:90px;height:146px;border:1px solid #b8e6f3"><div style="background:#1f8fe8;font-size:5px;text-align:center;padding:4px;color:#fff">RECOMMENDATION<br>B</div></div>
  <div class="abs" style="left:256px;top:56px;width:86px;height:134px;border:1px solid #b8e6f3"><div style="background:#d7f6f3;font-size:5px;text-align:center;padding:4px;color:var(--ink)">RECOMMENDATION<br>C</div></div>
  <div class="tiny abs" style="left:44px;top:86px;width:86px;text-align:center;line-height:2.2">First feature<br>Second feature<br>Third feature<br>Fourth feature<br>Fifth feature</div>
  <div class="tiny abs" style="left:148px;top:86px;width:90px;text-align:center;line-height:2.2">First feature<br>Second feature<br>Third feature<br>Fourth feature<br>Fifth feature</div>
  <div class="tiny abs" style="left:256px;top:86px;width:86px;text-align:center;line-height:2.2">First feature<br>Second feature<br>Third feature<br>Fourth feature<br>Fifth feature</div>
</section>

<section class="slide" style="left:801px;top:2643px">
  <div class="title" style="left:14px;top:12px"><b>PROJECT </b>OVERALL</div>
  <p class="tiny abs" style="left:14px;top:26px;width:350px;font-size:5.5px">Add a short summary of overall project figures here.</p>
  <table class="abs" style="left:30px;top:52px;width:324px;font-size:5px;color:var(--ink);text-align:center">
    <tr style="background:#1f8fe8;color:#fff"><td style="padding:2px">&nbsp;</td><td>Column 01</td><td>Column 02</td><td>Column 03</td><td>Column 04</td></tr>
    <tr style="height:19px;border-bottom:1px solid #eef2f5"><td>First Row</td><td>140,000</td><td>140,000</td><td>140,000</td><td>140,000</td></tr>
    <tr style="height:19px;border-bottom:1px solid #eef2f5"><td>Second Row</td><td>240,000</td><td>240,000</td><td>240,000</td><td>240,000</td></tr>
    <tr style="height:19px;border-bottom:1px solid #eef2f5"><td>Third Row</td><td>275,500</td><td>275,500</td><td>275,500</td><td>275,500</td></tr>
    <tr style="height:19px;border-bottom:1px solid #eef2f5"><td>Forth Row</td><td>350,000</td><td>350,000</td><td>350,000</td><td>350,000</td></tr>
    <tr style="height:19px;border-bottom:1px solid #eef2f5"><td>Fifth Row</td><td>420,400</td><td>420,400</td><td>420,400</td><td>420,400</td></tr>
    <tr style="height:19px"><td>Total</td><td>1,440,000</td><td>1,440,000</td><td>1,440,000</td><td>1,440,000</td></tr>
  </table>
</section>

<!-- Row 13 -->
<section class="slide" style="left:9px;top:2902px">
  <div class="abs mint-bg" style="inset:0"></div>
  <div class="frame" style="left:80px;top:60px;width:100px;height:90px"></div>
  <div class="divider-title" style="left:120px;top:74px">BUSINESS<br>ANALYSIS <span style="font-size:14px;color:var(--blue)">&#9680;</span></div>
</section>

<section class="slide" style="left:405px;top:2902px">
  <div class="title" style="left:14px;top:12px"><b>SWOT </b>ANALYSIS</div>
  <svg class="abs" style="left:132px;top:52px" width="120" height="120" viewBox="0 0 120 120">
    <path d="M24 60 A36 36 0 0 1 60 24 V40 A20 20 0 0 0 40 60Z" fill="#5fe0d3"/>
    <path d="M60 24 A36 36 0 0 1 96 60 H80 A20 20 0 0 0 60 40Z" fill="#1f8fe8"/>
    <path d="M96 60 A36 36 0 0 1 60 96 V80 A20 20 0 0 0 80 60Z" fill="#2ab5c8"/>
    <path d="M60 96 A36 36 0 0 1 24 60 H40 A20 20 0 0 0 60 80Z" fill="#3b5fb8"/>
    <g font-family="Questrial,sans-serif" font-size="12" text-anchor="middle" fill="#3d4b5c"><text x="14" y="64">S</text><text x="60" y="14" fill="#1f8fe8">T</text><text x="108" y="64">O</text><text x="60" y="114" fill="#3b5fb8">W</text></g>
  </svg>
  <div class="label abs" style="left:30px;top:58px">STRENGTHS</div><p class="tiny abs" style="left:30px;top:66px;width:80px">Add a short point here.</p>
  <div class="label abs" style="left:290px;top:58px">THREATS</div><p class="tiny abs" style="left:290px;top:66px;width:80px">Add a short point here.</p>
  <div class="label abs" style="left:30px;top:148px">WEAKNESS</div><p class="tiny abs" style="left:30px;top:156px;width:80px">Add a short point here.</p>
  <div class="label abs" style="left:290px;top:148px">OPPORTUNITIES</div><p class="tiny abs" style="left:290px;top:156px;width:80px">Add a short point here.</p>
</section>

<section class="slide" style="left:801px;top:2902px">
  <div class="title" style="left:14px;top:12px"><b>GROWTH </b>ANALYSIS</div>
  <div class="label abs" style="left:30px;top:48px;color:var(--ink)">Add Title here</div>
  <p class="tiny abs" style="left:30px;top:60px;width:70px">Add a short note on growth across each of the areas shown here.</p>
  <svg class="abs" style="left:120px;top:40px" width="160" height="150" viewBox="0 0 160 150">
    <g fill="none" stroke-width="10">
      <path d="M80 10 A65 65 0 1 1 22 102" stroke="#5fe0d3"/>
      <path d="M80 26 A49 49 0 1 1 37 96" stroke="#2ab5c8"/>
      <path d="M80 42 A33 33 0 1 1 50 88" stroke="#1f8fe8"/>
      <path d="M80 58 A17 17 0 1 1 64 80" stroke="#5a56b0"/>
    </g>
  </svg>
  <div class="dot" style="left:266px;top:50px;width:14px;height:14px;background:#5fe0d3"></div><div class="abs" style="left:286px;top:48px;font-size:9px">33%</div>
  <div class="dot" style="left:266px;top:84px;width:14px;height:14px;background:#2ab5c8"></div><div class="abs" style="left:286px;top:82px;font-size:9px">76%</div>
  <div class="dot" style="left:266px;top:118px;width:14px;height:14px;background:#1f8fe8"></div><div class="abs" style="left:286px;top:116px;font-size:9px">64%</div>
  <div class="dot" style="left:266px;top:152px;width:14px;height:14px;background:#5a56b0"></div><div class="abs" style="left:286px;top:150px;font-size:9px">50%</div>
</section>

<!-- Row 14 -->
<section class="slide" style="left:9px;top:3151px">
  <div class="photo" style="left:20px;top:20px;width:340px;height:130px;background:linear-gradient(90deg,#9fe9e1,#f6a24a,#e66c8f,#6d7fd6)" role="img" aria-label="Colourful world map with region markers"></div>
  <div class="dot" style="left:70px;top:34px;width:36px;height:36px;background:#5fe0d3;color:#fff;font-size:9px;text-align:center;line-height:36px">56k</div>
  <div class="dot" style="left:190px;top:54px;width:30px;height:30px;background:#2ab5c8;color:#fff;font-size:8px;text-align:center;line-height:30px">11k</div>
  <div class="dot" style="left:262px;top:28px;width:26px;height:26px;background:#5fe0d3;color:#fff;font-size:8px;text-align:center;line-height:26px">14k</div>
  <div class="dot" style="left:100px;top:96px;width:28px;height:28px;background:#2ab5c8;color:#fff;font-size:8px;text-align:center;line-height:28px">21k</div>
  <div class="dot" style="left:300px;top:96px;width:28px;height:28px;background:#5fe0d3;color:#fff;font-size:8px;text-align:center;line-height:28px">31k</div>
  <div class="title" style="left:6px;top:156px;font-size:10px"><b>MARKET </b>ANALYSIS</div>
  <div class="abs" style="left:0;top:170px;width:384px;height:40px;border-top:1px solid var(--line)"></div>
  <p class="tiny abs" style="left:14px;top:176px;width:100px">Add a short note about this region.</p>
  <div class="abs" style="left:170px;top:178px;width:12px;height:12px;background:var(--ink)"></div>
  <p class="tiny abs" style="left:188px;top:176px;width:80px">Add a short note about this region.</p>
  <div class="abs" style="left:286px;top:178px;width:12px;height:12px;background:var(--ink)"></div>
  <p class="tiny abs" style="left:302px;top:176px;width:74px">Add a short note here.</p>
</section>

<section class="slide" style="left:405px;top:3151px">
  <div class="photo ph-light" style="inset:0" role="img" aria-label="Faded office scene behind the chart"></div>
  <div class="title" style="left:220px;top:14px;font-size:10px"><b>COMPETITORS </b>ANALYSIS</div>
  <div class="abs" style="left:40px;top:30px;width:1px;height:150px;background:#9fb3c4"></div>
  <div class="abs" style="left:40px;top:180px;width:320px;height:1px;background:#9fb3c4"></div>
  <div class="abs" style="left:-24px;top:100px;transform:rotate(-90deg);font-size:5.5px;width:110px;text-align:center;color:var(--ink)">MARKET SIMILARITY</div>
  <div class="tiny abs" style="left:150px;top:184px;color:var(--ink)">COMPANY PROFILE</div>
  <div class="tiny abs" style="left:50px;top:184px;color:var(--ink)">Different</div>
  <div class="tiny abs" style="left:330px;top:184px;color:var(--ink)">Similar</div>
  <div class="dot" style="left:270px;top:40px;width:30px;height:30px;background:#7ad27a;color:#fff;font-size:8px;text-align:center;line-height:30px">D</div>
  <div class="dot" style="left:122px;top:68px;width:28px;height:28px;background:#1f8fe8;color:#fff;font-size:8px;text-align:center;line-height:28px">B</div>
  <div class="dot" style="left:200px;top:98px;width:34px;height:34px;background:#b45fd0;color:#fff;font-size:8px;text-align:center;line-height:34px">C</div>
  <div class="dot" style="left:74px;top:132px;width:32px;height:32px;background:#f6a24a;color:#fff;font-size:8px;text-align:center;line-height:32px">A</div>
  <div class="dot" style="left:268px;top:112px;width:18px;height:18px;background:#e66c8f;color:#fff;font-size:6px;text-align:center;line-height:18px">E</div>
</section>

<section class="slide" style="left:801px;top:3151px">
  <div class="photo ph-blue" style="left:150px;top:60px;width:234px;height:150px;clip-path:polygon(30% 100%,100% 0,100% 100%)" role="img" aria-label="Wave of blue glass squares"></div>
  <div class="box-blue" style="left:14px;top:14px;width:140px;height:120px;padding:10px;background:#6bc9f0;color:#0d1f3a">
    <div class="section-no">04.</div>
    <div class="section-name" style="margin-top:6px">Way<br>Forward</div>
    <ul class="list" style="margin-top:8px"><li>Our 2018 agenda</li></ul>
  </div>
</section>

<!-- Row 15 -->
<section class="slide" style="left:9px;top:3402px">
  <div class="photo ph-light" style="left:200px;top:0;width:184px;height:218px" role="img" aria-label="Stethoscope on a white surface"></div>
  <div class="title" style="left:14px;top:36px;font-size:10px"><b>OUR </b>2018 AGENDA</div>
  <div class="photo" style="left:140px;top:60px;width:110px;height:120px;background:linear-gradient(135deg,#5fe0d3,#3b5fb8)" role="img" aria-label="Four interlocking 3D puzzle blocks"></div>
  <div class="abs" style="left:150px;top:82px;font-size:12px;color:#fff">1</div>
  <div class="abs" style="left:236px;top:86px;font-size:12px;color:#fff">3</div>
  <div class="abs" style="left:164px;top:142px;font-size:12px;color:#fff">2</div>
  <div class="abs" style="left:240px;top:150px;font-size:12px;color:#fff">4</div>
  <div class="label abs" style="left:60px;top:80px">Insert title here</div><p class="tiny abs" style="left:40px;top:90px;width:90px">Add a short goal here.</p>
  <div class="label abs" style="left:270px;top:80px">Insert title here</div><p class="tiny abs" style="left:270px;top:90px;width:90px">Add a short goal here.</p>
  <div class="label abs" style="left:60px;top:150px">Insert title here</div><p class="tiny abs" style="left:40px;top:160px;width:90px">Add a short goal here.</p>
  <div class="label abs" style="left:270px;top:150px">Insert title here</div><p class="tiny abs" style="left:270px;top:160px;width:90px">Add a short goal here.</p>
</section>

<section class="slide" style="left:405px;top:3402px">
  <div class="photo" style="inset:0;background:linear-gradient(135deg,#6fb9d0,#e8c48a 60%,#7fc9d6)" role="img" aria-label="Blurred light trails in motion"></div>
  <div class="abs" style="left:14px;top:90px;font-size:11px;color:var(--ink)">OUR <span style="color:var(--navy)">2018 AGENDA</span></div>
</section>

<section class="slide" style="left:801px;top:3402px">
  <div class="photo ph-light" style="inset:0" role="img" aria-label="Faded office scene"></div>
  <div class="title" style="left:40px;top:40px;font-size:10px"><b>OUR </b>2018 AGENDA</div>
  <svg class="abs" style="left:60px;top:50px" width="320" height="120" viewBox="0 0 320 120">
    <path d="M10 110 L60 100 L110 90 L160 70 L210 55 L250 30 L260 18 L300 24 L280 40 L276 34 L220 66 L170 82 L120 100 L70 112 Z" fill="#1f8fe8"/>
    <g fill="#fff" stroke="#7f95a8" stroke-width="1.5">
      <circle cx="34" cy="86" r="12"/><circle cx="96" cy="74" r="12"/><circle cx="154" cy="54" r="12"/><circle cx="206" cy="36" r="12"/><circle cx="250" cy="12" r="11"/>
    </g>
    <g font-family="Questrial,sans-serif" font-size="10" fill="#3d4b5c" text-anchor="middle">
      <text x="34" y="90">01</text><text x="96" y="78">02</text><text x="154" y="58">03</text><text x="206" y="40">04</text><text x="250" y="16">05</text>
    </g>
  </svg>
  <p class="tiny abs" style="left:60px;top:174px;width:60px">Add a short goal here.</p>
  <p class="tiny abs" style="left:130px;top:150px;width:60px">Add a short goal here.</p>
  <p class="tiny abs" style="left:200px;top:126px;width:60px">Add a short goal here.</p>
  <p class="tiny abs" style="left:290px;top:100px;width:60px">Add a short goal here.</p>
</section>

<!-- Row 16 -->
<section class="slide" style="left:9px;top:3647px">
  <div class="title" style="left:14px;top:12px"><b>TEXT &amp; </b>BULLET POINTS</div>
  <div class="abs" style="left:14px;top:34px;width:356px;height:170px;border:1px solid #b8e6f3"></div>
  <p class="abs" style="left:28px;top:80px;width:70px;font-size:6px;line-height:1.35;color:var(--ink)">Add a short paragraph here to introduce the points listed on this slide.</p>
  <div class="abs" style="left:118px;top:54px;display:grid;grid-template-columns:110px 110px;row-gap:18px;font-size:6px;color:var(--ink)">
    <span><i style="display:inline-block;width:12px;height:12px;background:#2ab5c8;vertical-align:middle;margin-right:8px"></i>The subtitle</span>
    <span><i style="display:inline-block;width:12px;height:12px;background:#5fe0d3;vertical-align:middle;margin-right:8px"></i>The subtitle</span>
    <span><i style="display:inline-block;width:12px;height:12px;background:#1f8fe8;vertical-align:middle;margin-right:8px"></i>The subtitle</span>
    <span><i style="display:inline-block;width:12px;height:12px;background:#e66c8f;vertical-align:middle;margin-right:8px"></i>The subtitle</span>
    <span><i style="display:inline-block;width:12px;height:12px;background:#3d4b5c;vertical-align:middle;margin-right:8px"></i>The subtitle</span>
    <span><i style="display:inline-block;width:12px;height:12px;background:#7ad27a;vertical-align:middle;margin-right:8px"></i>The subtitle</span>
    <span><i style="display:inline-block;width:12px;height:12px;background:#2c5ea8;vertical-align:middle;margin-right:8px"></i>The subtitle</span>
    <span><i style="display:inline-block;width:12px;height:12px;background:#f6a24a;vertical-align:middle;margin-right:8px"></i>The subtitle</span>
  </div>
</section>

<section class="slide" style="left:405px;top:3647px">
  <div class="photo ph-teal" style="inset:0" role="img" aria-label="Soft teal background with a light circle"></div>
  <div class="dot" style="left:112px;top:30px;width:160px;height:160px;background:rgba(255,255,255,.55)"></div>
  <div class="abs" style="left:112px;top:62px;width:160px;text-align:center;font-size:42px;color:#2f7fb4;letter-spacing:-1px">Q&amp;A</div>
  <div class="abs" style="left:112px;top:122px;width:160px;text-align:center;font-size:8px;color:var(--ink);line-height:1.3">Do you have any question?<br>Feel free to ask.</div>
</section>

<section class="slide" style="left:801px;top:3647px">
  <div class="photo ph-teal" style="left:0;top:0;width:384px;height:130px" role="img" aria-label="Business people shaking hands"></div>
  <div class="abs" style="left:0;top:50px;width:384px;text-align:center;font-size:12px;color:#fff;letter-spacing:1px">THANK YOU</div>
  <div class="abs" style="left:0;top:130px;width:384px;height:80px;background:#e4fcf9"></div>
  <div class="title" style="left:24px;top:140px;font-size:8px"><b>OUR </b>CONTACT</div>
  <div class="dot" style="left:24px;top:156px;width:8px;height:8px;background:var(--blue)"></div>
  <p class="tiny abs" style="left:36px;top:156px;width:80px">Add your address here.</p>
  <div class="dot" style="left:150px;top:164px;width:8px;height:8px;background:var(--blue)"></div>
  <p class="tiny abs" style="left:162px;top:164px;width:60px">Phone number</p>
  <div class="dot" style="left:250px;top:164px;width:8px;height:8px;background:var(--blue)"></div>
  <p class="tiny abs" style="left:262px;top:164px;width:80px">Web page</p>
</section>

</body>
</html>
```